Redesign - Trifold Brochure - Adding new and fresh look.

I have attached what we currently have as a brochure but we need it to be redesigned. The information content is accurate but looking for fresh new design/layout. Please see the images attached. In tif and pdf format. If you need a different format to work please specify and will do my best to upload it.

Target Market(s)

Retail giveaways to educate customers.

Requirements
Must have
• New fresh look

```html
<!DOCTYPE html>
<html lang="en">
<head>
<meta charset="utf-8">
<title>Verdant Roots – Trifold Brochure</title>
<link href="https://fonts.googleapis.com/css2?family=Open+Sans:wght@400;600;700;800&display=swap" rel="stylesheet">
<style>
  :root{
    --bg:#3a3a3c;
    --orange:#f39a12;
    --orange-deep:#ea7a0c;
    --green:#a3c93a;
    --green-deep:#86ad22;
    --grey:#cfd3d6;
    --grey-dark:#8d9295;
    --white:#ffffff;
    --navy:#0f2a35;
    --navy-deep:#081a22;
    --ink:#2b2b2b;
  }
  *{box-sizing:border-box;margin:0;padding:0}
  html,body{width:800px;height:1200px;overflow:hidden}
  body{background:var(--bg);font-family:"Open Sans",Arial,sans-serif;color:var(--white);position:relative}
  .brochure{position:absolute;left:20px;width:760px;height:540px;display:flex;overflow:hidden;box-shadow:0 10px 30px rgba(0,0,0,.45)}
  .brochure--outside{top:20px}
  .brochure--inside{top:630px}
  .panel{position:relative;width:253.33px;height:100%;overflow:hidden}
  .wave{position:absolute;left:0;width:100%}
  .placeholder{position:absolute}
  .brand{display:flex;align-items:center;justify-content:center;gap:6px;font-weight:600;color:var(--green-deep)}
  .brand__dot{width:14px;height:14px;border-radius:50%;background:var(--orange)}
  .web{font-weight:600;font-size:10px;color:var(--white)}
  .web b{font-weight:800}

  /* outside – left */
  .qa{background:var(--orange)}
  .qa .photo{left:0;top:0;width:100%;height:120px;background:radial-gradient(circle at 55% 45%,#f4e08a,#c9a84a 45%,#e9e9e9 75%)}
  .qa__body{position:absolute;left:16px;right:14px;top:130px;font-size:8.6px;line-height:1.28}
  .qa__intro{font-weight:700;font-size:9px;color:var(--ink);margin-bottom:6px}
  .qa__title{font-size:11px;font-weight:400;line-height:1.2;margin-bottom:6px}
  .qa__title b{font-weight:800;display:block}
  .qa h3{font-size:10px;font-weight:700;margin:5px 0 1px;display:flex;align-items:center;gap:4px}
  .tick{width:10px;height:10px;flex:none}
  .qa .web{position:absolute;left:0;right:0;bottom:12px;text-align:center}

  /* outside – middle */
  .contact{background:var(--white)}
  .contact .brand{position:absolute;top:22px;left:0;right:0;font-size:11px}
  .contact .photo{left:40px;top:55px;width:175px;height:175px;border-radius:6px;background:linear-gradient(160deg,#f2f2f2,#d8d8d8 40%,#5b3a1c 70%,#2a1a0c)}
  .contact__text{position:absolute;left:16px;right:16px;top:262px;text-align:center;font-size:9px;line-height:1.35;color:var(--ink)}
  .contact__text p{margin-bottom:10px}
  .contact__text strong{display:block;color:var(--white);font-weight:700;font-size:10px}
  .phone{display:flex;align-items:center;justify-content:center;gap:6px;margin:6px auto 6px;width:200px;height:28px;border:1.5px solid var(--white);border-radius:14px;font-size:15px;font-weight:800;color:var(--ink)}
  .contact .web{display:block;text-align:center;color:var(--white)}

  /* outside – cover */
  .cover{background:var(--white)}
  .cover .brand{position:absolute;top:42px;left:0;right:0;font-size:15px}
  .cover__tagline{position:absolute;top:68px;left:0;right:0;text-align:center;font-size:8.5px;color:var(--ink)}
  .cover .photo{left:0;top:95px;width:100%;height:225px;background:radial-gradient(circle at 50% 50%,#6b8f3a,#a8c277 45%,#eef2e6 80%)}
  .cover__text{position:absolute;left:0;right:0;top:375px;text-align:center}
  .cover__kicker{font-size:11px;margin-bottom:8px}
  .cover__title{font-size:15px;font-weight:800;line-height:1.2}
  .rule{width:40px;height:2px;background:var(--white);margin:8px auto}

  /* inside – left */
  .about{background:var(--green)}
  .about .photo{left:0;top:0;width:100%;height:300px;background:linear-gradient(170deg,#f6b42a,#c26a12 35%,#e9d7b5 65%,#c9b08a)}
  .about__body{position:absolute;left:18px;right:14px;top:330px;font-size:8.6px;line-height:1.3}
  .about h3{font-size:11px;font-weight:700;display:flex;align-items:center;gap:5px;margin-bottom:4px}
  .about ul{list-style:none;margin-top:6px;font-weight:700;font-size:9.5px}
  .about li{display:flex;align-items:center;gap:5px;line-height:1.35}

  /* inside – spread */
  .spread{position:relative;width:506.67px;height:100%;background:linear-gradient(90deg,var(--navy-deep),var(--navy) 45%,#3a1a14 85%,#5a1e12)}
  .spread .figure{left:40px;top:20px;width:170px;height:330px;border-radius:80px 80px 20px 20px;background:radial-gradient(ellipse at 50% 45%,rgba(120,200,230,.55),rgba(40,110,140,.25) 55%,transparent 75%)}
  .spread .organ{left:300px;top:120px;width:200px;height:170px;border-radius:50%;background:radial-gradient(circle,rgba(200,70,40,.7),rgba(120,30,20,.3) 55%,transparent 75%)}
  .callout{position:absolute;width:62px;height:62px;border-radius:50%;background:var(--orange);border:2px solid #f7c36b;display:flex;align-items:center;justify-content:center;text-align:center;font-size:5.4px;line-height:1.25;font-weight:600;color:var(--ink);padding:8px}
  .connector{position:absolute;left:0;top:0}
  .how{position:absolute;left:282px;top:25px;width:210px}
  .how h2{font-size:15px;font-weight:800;line-height:1.2;margin-bottom:6px}
  .how p{font-size:6.4px;line-height:1.35;opacity:.9}
  .spread .bottle{left:405px;top:230px;width:58px;height:190px;border-radius:10px 10px 6px 6px;background:linear-gradient(90deg,#e9e9e9,#ffffff 50%,#d6d6d6)}
  .benefits{position:absolute;left:20px;top:420px;width:250px}
  .benefits h2{font-size:11.5px;font-weight:800;line-height:1.22;margin-bottom:8px}
  .list{display:flex;gap:8px;align-items:stretch}
  .tag{background:var(--navy);color:var(--white);font-size:8px;font-weight:800;writing-mode:vertical-rl;transform:rotate(180deg);padding:4px 3px;text-align:center;letter-spacing:.5px}
  .list ul{list-style:none;font-size:9px;font-weight:600}
  .list li{display:flex;align-items:center;gap:5px;line-height:1.45}
  .low{position:absolute;left:290px;top:450px}
</style>
</head>
<body>

<!-- OUTSIDE -->
<section class="brochure brochure--outside">
  <article class="panel qa">
    <div class="placeholder photo" role="img" aria-label="Glass jar of hemp oil beside a wooden bowl of hemp seeds and a hemp leaf"></div>
    <svg class="wave" style="top:100px" width="254" height="40" viewBox="0 0 254 40" preserveAspectRatio="none"><path d="M0 40 L0 18 Q130 -4 254 10 L254 40Z" fill="#8d9295"/><path d="M0 40 L0 26 Q130 6 254 18 L254 40Z" fill="#f39a12"/></svg>
    <div class="qa__body">
      <p class="qa__intro">Hemp derived products are widely thought to be the most nutritionally complete supplement source in the world.</p>
      <p class="qa__title">The Most Common Questions <b>Associated with CBD Use:</b></p>
      <h3><svg class="tick" viewBox="0 0 10 10"><circle cx="5" cy="5" r="5" fill="#2b2b2b"/><path d="M2.5 5.2 4.3 7 7.6 3.4" stroke="#a3c93a" stroke-width="1.4" fill="none"/></svg>Will I get "high" or feel "loaded"?</h3>
      <p>The answer is, "No." Industrial hemp derived CBD will not make you feel euphoric. If you feel this way from a CBD product, it does not solely contain CBD and may contain synthetics or other compounds not listed on the label and should not be used.</p>
      <h3><svg class="tick" viewBox="0 0 10 10"><circle cx="5" cy="5" r="5" fill="#2b2b2b"/><path d="M2.5 5.2 4.3 7 7.6 3.4" stroke="#a3c93a" stroke-width="1.4" fill="none"/></svg>Is it legal?</h3>
      <p>Yes. Industrial hemp derived CBD contains very low to no THC levels which is the compound that makes Marijuana illegal. Industrial hemp products containing levels of THC ranging from 0% to 0.03% can be purchased from regular retailers and are legal in all 50 states.</p>
      <h3><svg class="tick" viewBox="0 0 10 10"><circle cx="5" cy="5" r="5" fill="#2b2b2b"/><path d="M2.5 5.2 4.3 7 7.6 3.4" stroke="#a3c93a" stroke-width="1.4" fill="none"/></svg>How can I take CBD?</h3>
      <p>CBD comes in many forms: Tinctures, edibles, vaporizable liquids, capsules, powders, as well as topical creams and salves.</p>
      <h3><svg class="tick" viewBox="0 0 10 10"><circle cx="5" cy="5" r="5" fill="#2b2b2b"/><path d="M2.5 5.2 4.3 7 7.6 3.4" stroke="#a3c93a" stroke-width="1.4" fill="none"/></svg>How much CBD should I take?</h3>
      <p>Lorem ipsum dolor sit amet, consectetur adipiscing elit, sed do eiusmod tempor incididunt ut labore et dolore magna aliqua.</p>
    </div>
    <p class="web">www.<b>verdantroots</b>.example</p>
  </article>

  <article class="panel contact">
    <svg class="wave" style="top:170px" width="254" height="370" viewBox="0 0 254 370" preserveAspectRatio="none"><path d="M0 40 Q120 0 254 20 L254 370 L0 370Z" fill="#cfd3d6"/><path d="M0 52 Q120 14 254 34 L254 370 L0 370Z" fill="#a3c93a"/></svg>
    <div class="brand"><span class="brand__dot"></span>Verdant Roots</div>
    <div class="placeholder photo" role="img" aria-label="Capsule jar and dropper bottle of hemp supplement products"></div>
    <div class="contact__text">
      <p>If you would like to receive more information or purchase Verdant Roots products, please contact: <strong>care@verdantroots.example</strong></p>
      <p>If you would like to become a wholesale partner of Verdant Roots, please send all wholesale inquiries to: <strong>trade@verdantroots.example</strong></p>
      <div class="phone"><svg width="14" height="14" viewBox="0 0 14 14"><circle cx="7" cy="7" r="6.3" fill="none" stroke="#2b2b2b" stroke-width="1.2"/><path d="M4.6 3.6c.4-.3.8-.2 1 .2l.6 1.2c.1.3 0 .6-.2.8l-.4.4c.4.9 1.1 1.6 2 2l.4-.4c.2-.2.5-.3.8-.2l1.2.6c.4.2.5.6.2 1-.6.8-1.6.9-2.4.5-1.6-.7-2.9-2-3.6-3.6-.4-.8-.3-1.8.4-2.5z" fill="#2b2b2b"/></svg>(800) 555-0142</div>
      <span class="web">www.<b>verdantroots</b>.example</span>
    </div>
  </article>

  <article class="panel cover">
    <div class="brand"><span class="brand__dot"></span>Verdant Roots</div>
    <p class="cover__tagline">Healthier Living Through Quality Products</p>
    <div class="placeholder photo" role="img" aria-label="Close-up of a green hemp plant with flowering buds"></div>
    <svg class="wave" style="top:290px" width="254" height="250" viewBox="0 0 254 250" preserveAspectRatio="none"><path d="M0 40 Q130 10 254 0 L254 250 L0 250Z" fill="#cfd3d6"/><path d="M0 52 Q130 22 254 14 L254 250 L0 250Z" fill="#f39a12"/><path d="M0 200 L254 170 L254 250 L0 250Z" fill="#ea7a0c"/></svg>
    <div class="cover__text">
      <p class="cover__kicker">Can CBD Products Help Me?</p>
      <p class="cover__title">Understanding<br>Your Endocannabinoid<br>System</p>
      <div class="rule"></div>
      <p class="web">www.<b>verdantroots</b>.example</p>
    </div>
  </article>
</section>

<!-- INSIDE -->
<section class="brochure brochure--inside">
  <article class="panel about">
    <div class="placeholder photo" role="img" aria-label="Golden hemp oil dripping from a spoon onto a wooden surface"></div>
    <svg class="wave" style="top:270px" width="254" height="270" viewBox="0 0 254 270" preserveAspectRatio="none"><path d="M0 40 Q120 0 254 10 L254 270 L0 270Z" fill="#cfd3d6"/><path d="M0 52 Q120 12 254 22 L254 270 L0 270Z" fill="#a3c93a"/></svg>
    <div class="about__body">
      <h3><svg class="tick" viewBox="0 0 10 10"><circle cx="5" cy="5" r="5" fill="#fff"/><path d="M2.5 5.2 4.3 7 7.6 3.4" stroke="#86ad22" stroke-width="1.4" fill="none"/></svg>What is CBD?</h3>
      <p>One of many compounds called phytocannabinoids that is found in various plant species. The industrial hemp plant is a plentiful source of CBD. When derived from industrial hemp, CBD with less than 0.03% THC by weight has no psychoactive properties but retains all of its positive bio-</p>
      <p style="margin-top:5px">CBD is commonly used as relief from:</p>
      <ul>
        <li><svg class="tick" viewBox="0 0 10 10"><circle cx="5" cy="5" r="5" fill="#fff"/><path d="M2.5 5.2 4.3 7 7.6 3.4" stroke="#86ad22" stroke-width="1.4" fill="none"/></svg>Pain</li>
        <li><svg class="tick" viewBox="0 0 10 10"><circle cx="5" cy="5" r="5" fill="#fff"/><path d="M2.5 5.2 4.3 7 7.6 3.4" stroke="#86ad22" stroke-width="1.4" fill="none"/></svg>Inflammation</li>
        <li><svg class="tick" viewBox="0 0 10 10"><circle cx="5" cy="5" r="5" fill="#fff"/><path d="M2.5 5.2 4.3 7 7.6 3.4" stroke="#86ad22" stroke-width="1.4" fill="none"/></svg>Anxiety</li>
        <li><svg class="tick" viewBox="0 0 10 10"><circle cx="5" cy="5" r="5" fill="#fff"/><path d="M2.5 5.2 4.3 7 7.6 3.4" stroke="#86ad22" stroke-width="1.4" fill="none"/></svg>Sleep Disorders</li>
        <li><svg class="tick" viewBox="0 0 10 10"><circle cx="5" cy="5" r="5" fill="#fff"/><path d="M2.5 5.2 4.3 7 7.6 3.4" stroke="#86ad22" stroke-width="1.4" fill="none"/></svg>Neurological Disorders</li>
        <li><svg class="tick" viewBox="0 0 10 10"><circle cx="5" cy="5" r="5" fill="#fff"/><path d="M2.5 5.2 4.3 7 7.6 3.4" stroke="#86ad22" stroke-width="1.4" fill="none"/></svg>Opiate Dependence</li>
      </ul>
    </div>
  </article>

  <article class="spread">
    <div class="placeholder figure" role="img" aria-label="Glowing blue illustration of a human body outline showing the nervous system"></div>
    <div class="placeholder organ" role="img" aria-label="Soft red glowing illustration of the brain and nerve network"></div>
    <svg class="connector" width="507" height="540" viewBox="0 0 507 540"><g stroke="#e8eef0" stroke-width="1" fill="none" opacity=".7"><path d="M150 95 L190 95"/><path d="M140 185 L200 195"/><path d="M150 305 L195 300"/><path d="M260 240 L330 250 L300 220"/></g></svg>
    <div class="callout" style="left:190px;top:65px">CB2 receptors are predominantly found in the immune system.</div>
    <div class="callout" style="left:200px;top:165px">CB1 and CB2 receptors are found on the surface of cells in your body.</div>
    <div class="callout" style="left:195px;top:270px">CB2 receptors are responsible for regulating inflammation which in turn reduces pain.</div>
    <div class="callout" style="left:330px;top:215px">CB1 receptors are found mostly in the brain, regulating mood, sleep, appetite and memory.</div>
    <div class="how">
      <h2>How Does CBD Work in Your Body?</h2>
      <p>Your body produces certain natural compounds called cannabinoids that are used to regulate functions for your entire body. Inside your body there is a processing network for cannabinoids called the Endocannabinoid System. CBD mimics the natural compounds produced by your body and stimulates receptors found on the surface of cells within your ECS, helping the immune and nervous systems restore your body's natural balance.</p>
    </div>
    <svg class="wave" style="top:355px" width="507" height="185" viewBox="0 0 507 185" preserveAspectRatio="none"><path d="M0 30 Q250 0 507 20 L507 185 L0 185Z" fill="#a3c93a"/><path d="M0 42 Q250 12 507 32 L507 185 L0 185Z" fill="#f39a12"/><path d="M0 160 L507 140 L507 185 L0 185Z" fill="#ea7a0c"/></svg>
    <div class="placeholder bottle" role="img" aria-label="White spray bottle of hemp extract oral spray"></div>
    <div class="benefits">
      <h2>There are many other benefits from using CBD and hemp products. Hemp products are:</h2>
      <div class="list">
        <span class="tag">HIGH IN</span>
        <ul>
          <li><svg class="tick" viewBox="0 0 10 10"><circle cx="5" cy="5" r="5" fill="#fff"/><path d="M2.5 5.2 4.3 7 7.6 3.4" stroke="#ea7a0c" stroke-width="1.4" fill="none"/></svg>Omega 3 and 6 Fatty Acids</li>
          <li><svg class="tick" viewBox="0 0 10 10"><circle cx="5" cy="5" r="5" fill="#fff"/><path d="M2.5 5.2 4.3 7 7.6 3.4" stroke="#ea7a0c" stroke-width="1.4" fill="none"/></svg>Vitamins A &amp; E</li>
          <li><svg class="tick" viewBox="0 0 10 10"><circle cx="5" cy="5" r="5" fill="#fff"/><path d="M2.5 5.2 4.3 7 7.6 3.4" stroke="#ea7a0c" stroke-width="1.4" fill="none"/></svg>Calcium, Iron &amp; Antioxidants</li>
        </ul>
      </div>
    </div>
    <div class="list low">
      <span class="tag">LOW IN</span>
      <ul>
        <li><svg class="tick" viewBox="0 0 10 10"><circle cx="5" cy="5" r="5" fill="#fff"/><path d="M2.5 5.2 4.3 7 7.6 3.4" stroke="#ea7a0c" stroke-width="1.4" fill="none"/></svg>Saturated Fats</li>
        <li><svg class="tick" viewBox="0 0 10 10"><circle cx="5" cy="5" r="5" fill="#fff"/><path d="M2.5 5.2 4.3 7 7.6 3.4" stroke="#ea7a0c" stroke-width="1.4" fill="none"/></svg>Cholesterol</li>
        <li><svg class="tick" viewBox="0 0 10 10"><circle cx="5" cy="5" r="5" fill="#fff"/><path d="M2.5 5.2 4.3 7 7.6 3.4" stroke="#ea7a0c" stroke-width="1.4" fill="none"/></svg>Carbohydrates</li>
      </ul>
    </div>
  </article>
</section>

</body>
</html>
```